Salon and Spa Distributor Business Card

Need a business card. We are are distributor in the salon and spa industry. We identify with natural beauty. Need a card with:
Company Name: Petal Haven"
Title: "President & CEO"
Address
Company Phone number
email
website
Tag Line:" The Professional Salon Source"

Industry/Entity Type

Business

Contact Information for Business Card

Name: Lena Morcott
Title: "President & CEO"
Address: 317 Birchfield Ln, Oakvane, NJ 07481
Company Phone number: 800-463-9152
email: lenamorcott@petalhaven-example.com
website: www.petalhaven-example.com

Requirements
Should not have
• No black backgrounds

```html
<!DOCTYPE html>
<html lang="en">
<head>
<meta charset="utf-8">
<title>Petal Haven Business Card</title>
<link rel="stylesheet" href="https://fonts.googleapis.com/css2?family=Quicksand:wght@400;500;700&display=swap">
<style>
  :root {
    --bg: #e9ece9;
    --green-light: #5db54a;
    --green-mid: #3f9f4e;
    --green-deep: #2f8a58;
    --green-dark: #1f7a3a;
    --green-brand: #6cbf5a;
    --grey-text: #555a58;
    --white: #ffffff;
    --leaf-soft: rgba(150, 210, 120, 0.55);
    --leaf-faint: rgba(120, 180, 110, 0.14);
  }
  * { margin: 0; padding: 0; box-sizing: border-box; }
  html, body {
    width: 1200px; height: 1200px; overflow: hidden;
    background: var(--bg);
    font-family: "Quicksand", sans-serif;
  }
  .canvas { position: relative; width: 1200px; height: 1200px; }
  .card {
    position: absolute; left: 150px; width: 900px; height: 514px;
    overflow: hidden; border-radius: 4px;
    box-shadow: 0 8px 24px rgba(0,0,0,0.12);
  }
  /* Front */
  .card-front {
    top: 60px;
    background: linear-gradient(135deg, var(--green-light) 0%, var(--green-mid) 55%, var(--green-deep) 100%);
  }
  .front-brand { position: absolute; left: 120px; top: 200px; color: var(--white); }
  .front-brand .mark {
    display: inline-block; width: 22px; height: 22px; border-radius: 50%;
    background: var(--white); vertical-align: middle; margin-right: 14px;
  }
  .front-brand .brand-name {
    font-size: 56px; font-weight: 500; vertical-align: middle; letter-spacing: 0.5px;
  }
  .front-brand .tagline {
    font-size: 22px; font-weight: 500; margin: 10px 0 0 38px;
  }
  .front-leaves {
    position: absolute; right: -40px; top: 150px; width: 380px; height: 380px;
    border-radius: 60% 0 60% 40%;
    background: radial-gradient(circle at 40% 40%, var(--leaf-soft), rgba(90,180,80,0) 70%);
  }
  /* Back */
  .card-back { top: 626px; background: var(--white); }
  .back-leaves {
    position: absolute; right: 40px; top: 130px; width: 380px; height: 360px;
    border-radius: 50% 10% 50% 40%;
    background: radial-gradient(circle at 50% 45%, var(--leaf-faint), rgba(255,255,255,0) 72%);
  }
  .back-brand {
    position: absolute; left: 430px; top: 80px; color: var(--green-brand);
    font-size: 46px; font-weight: 500;
  }
  .back-brand .mark {
    display: inline-block; width: 18px; height: 18px; border-radius: 50%;
    background: var(--green-brand); vertical-align: middle; margin-right: 12px;
  }
  .back-brand span { vertical-align: middle; }
  .person { position: absolute; left: 60px; top: 180px; }
  .person-name { font-size: 40px; font-weight: 700; color: var(--green-dark); letter-spacing: -0.5px; }
  .person-title { font-size: 22px; font-weight: 500; color: var(--grey-text); margin: 4px 0 0 10px; }
  .address {
    position: absolute; right: 50px; top: 300px; text-align: right;
    font-size: 22px; font-weight: 500; color: var(--grey-text); line-height: 1.45;
    font-style: normal;
  }
  .address svg { vertical-align: -2px; margin-left: 6px; }
  .contacts { position: absolute; left: 60px; top: 388px; list-style: none; }
  .contacts li {
    font-size: 22px; font-weight: 500; color: var(--grey-text);
    height: 36px; display: flex; align-items: center; gap: 10px;
  }
  .contacts svg { flex: none; }
</style>
</head>
<body>
<main class="canvas">
  <section class="card card-front">
    <div class="front-leaves" role="img" aria-label="Soft green leaf illustration"></div>
    <div class="front-brand">
      <span class="mark"></span><span class="brand-name">Petal Haven</span>
      <p class="tagline">The Professional Salon Source</p>
    </div>
  </section>

  <section class="card card-back">
    <div class="back-leaves" role="img" aria-label="Faint green leaf illustration"></div>
    <div class="back-brand"><span class="mark"></span><span>Petal Haven</span></div>
    <div class="person">
      <h1 class="person-name">LENA MORCOTT</h1>
      <p class="person-title">President &amp; CEO</p>
    </div>
    <address class="address">
      317 Birchfield Ln
      <svg width="20" height="20" viewBox="0 0 20 20"><path d="M10 2 L19 10 H16 V18 H12 V13 H8 V18 H4 V10 H1 Z" fill="var(--green-light)"/></svg><br>
      Oakvane, NJ 07481
    </address>
    <ul class="contacts">
      <li>
        <svg width="20" height="20" viewBox="0 0 20 20"><path d="M4 2 L8 2 L9 6 L7 8 C8 11 9 12 12 13 L14 11 L18 12 L18 16 C18 17 17 18 16 18 C8 18 2 12 2 4 C2 3 3 2 4 2 Z" fill="var(--green-light)"/></svg>
        800-463-9152
      </li>
      <li>
        <svg width="20" height="20" viewBox="0 0 20 20"><circle cx="10" cy="10" r="8" fill="none" stroke="var(--green-light)" stroke-width="2"/><path d="M2 10 H18 M10 2 C6 6 6 14 10 18 M10 2 C14 6 14 14 10 18" fill="none" stroke="var(--green-light)" stroke-width="1.5"/></svg>
        www.petalhaven-example.com
      </li>
      <li>
        <svg width="20" height="20" viewBox="0 0 20 20"><rect x="2" y="4" width="16" height="12" rx="1" fill="var(--green-light)"/><path d="M2 5 L10 11 L18 5" fill="none" stroke="var(--white)" stroke-width="1.5"/></svg>
        lenamorcott@petalhaven-example.com
      </li>
    </ul>
  </section>
</main>
</body>
</html>
```